Timbrafix de México
Imprimiendo Ideas
Corporate
Rodrigo Salcedo Imaz
CEO
17 de Octubre 583 Loc. B-7 Col. Pradera, Deleg. Tlalmiro, México, D.F.
4857-3160 Vocalta
rodrigosalcedo@timbrafix-ejemplo.com.mx
ww.timbrafix-ejemplo.com.mx
Tarjetas * Postales * Volantes *
* Folders * Revistas

```html
<!DOCTYPE html>
<html lang="es">
<head>
<meta charset="utf-8">
<title>Timbrafix de México – Tarjetas</title>
<link href="https://fonts.googleapis.com/css2?family=Arimo:wght@400;700&display=swap" rel="stylesheet">
<style>
  :root {
    --brand-blue: #1a5bb8;
    --brand-blue-deep: #1049a3;
    --brand-red: #e4202a;
    --card-red: #e32228;
    --ink: #333333;
    --white: #ffffff;
    --canvas: #ffffff;
    --frame: #c9c9c9;
    --faint: #eef2f8;
  }
  * { margin: 0; padding: 0; box-sizing: border-box; }
  html, body { width: 1200px; height: 725px; overflow: hidden; background: var(--canvas); }
  body { position: relative; font-family: "Arimo", Arial, sans-serif; }

  .card { position: absolute; width: 545px; height: 318px; overflow: hidden; }
  .card--front { left: 43px; top: 43px; background: var(--white); border: 1px solid var(--frame); }
  .card--blue  { left: 612px; top: 43px; background: var(--brand-blue); }
  .card--white { left: 43px; top: 389px; background: var(--white); border: 1px solid var(--frame); }
  .card--red   { left: 612px; top: 389px; background: var(--card-red); }

  .edge { position: absolute; left: 0; width: 100%; height: 14px; }
  .edge--top { top: 0; }
  .edge--bottom { bottom: 0; }

  .brand { position: absolute; display: flex; flex-direction: column; }
  .brand__row { display: flex; align-items: center; gap: 9px; }
  .brand__dot { width: 28px; height: 28px; border-radius: 50%; background: var(--brand-blue); flex: none; }
  .brand__name { font-weight: 700; font-size: 25px; line-height: 30px; color: var(--brand-blue); white-space: nowrap; }
  .brand__tagline { font-weight: 700; font-size: 15px; line-height: 18px; color: var(--brand-red); margin-top: 2px; white-space: nowrap; }

  .card--blue .brand__name, .card--red .brand__name { color: var(--white); }
  .card--blue .brand__dot, .card--red .brand__dot { background: var(--white); }
  .card--red .brand__tagline { color: var(--brand-blue-deep); }

  /* front */
  .card--front .brand { left: 30px; top: 84px; }
  .card--front .brand__name { font-size: 22px; }
  .card--front .brand__dot { width: 24px; height: 24px; }
  .card--front .brand__tagline { font-size: 13px; margin-left: 70px; }

  .faint-mark { position: absolute; left: 420px; top: 215px; width: 80px; height: 80px; border-radius: 50%; background: var(--faint); }

  .person { position: absolute; left: 262px; top: 168px; text-align: right; width: 250px; }
  .person__name { font-size: 20px; line-height: 24px; color: var(--brand-red); white-space: nowrap; }
  .person__role { font-size: 11px; color: var(--ink); text-align: center; margin-left: 70px; margin-top: 1px; }

  .contact { position: absolute; left: 24px; top: 190px; font-size: 11.5px; line-height: 16px; color: var(--ink); font-style: normal; white-space: nowrap; }
  .contact__web { color: var(--brand-red); }

  /* backs */
  .services { position: absolute; font-size: 18px; line-height: 26px; text-align: center; white-space: nowrap; }
  .card--blue .services { left: 250px; width: 270px; top: 234px; color: var(--white); }
  .card--white .services { left: 0; width: 100%; top: 220px; color: var(--brand-blue); }
  .card--red .services { left: 0; width: 100%; top: 222px; color: var(--white); }

  .card--blue .brand { left: 14px; top: 118px; align-items: center; }
  .card--white .brand, .card--red .brand { left: 0; width: 100%; top: 110px; align-items: center; }
</style>
</head>
<body>

<section class="card card--front">
  <svg class="edge edge--top" viewBox="0 0 545 14" preserveAspectRatio="none">
    <rect x="0" y="6" width="545" height="5" fill="var(--brand-blue)"/>
    <rect x="410" y="0" width="28" height="11" fill="var(--brand-red)"/>
    <rect x="446" y="0" width="17" height="11" fill="var(--brand-red)"/>
    <rect x="471" y="0" width="17" height="11" fill="var(--brand-red)"/>
    <rect x="496" y="0" width="17" height="11" fill="var(--brand-red)"/>
    <rect x="521" y="0" width="24" height="11" fill="var(--brand-red)"/>
  </svg>
  <div class="faint-mark" aria-hidden="true"></div>
  <div class="brand">
    <div class="brand__row"><span class="brand__dot"></span><span class="brand__name">Timbrafix de México</span></div>
    <div class="brand__tagline">Imprimiendo Ideas</div>
  </div>
  <div class="person">
    <div class="person__name">Rodrigo Salcedo Imaz</div>
    <div class="person__role">CEO</div>
  </div>
  <address class="contact">
    17 de Octubre 583 Loc. B-7 Col. Pradera<br>
    Deleg. Tlalmiro, México, D.F.<br>
    Phone: 0155-6042-3391 * 6290-4471 * 6613-0928<br>
    Cell: 4857-3160 Vocalta<br>
    Email: rodrigosalcedo@timbrafix-ejemplo.com.mx<br>
    <span class="contact__web">www.timbrafix-ejemplo.com.mx</span>
  </address>
  <svg class="edge edge--bottom" viewBox="0 0 545 14" preserveAspectRatio="none">
    <rect x="0" y="3" width="545" height="5" fill="var(--brand-blue)"/>
    <rect x="0" y="3" width="24" height="11" fill="var(--brand-red)"/>
    <rect x="32" y="3" width="17" height="11" fill="var(--brand-red)"/>
    <rect x="57" y="3" width="17" height="11" fill="var(--brand-red)"/>
    <rect x="82" y="3" width="17" height="11" fill="var(--brand-red)"/>
  </svg>
</section>

<section class="card card--blue">
  <div class="brand">
    <div class="brand__row"><span class="brand__dot"></span><span class="brand__name">Timbrafix de México</span></div>
    <div class="brand__tagline">Imprimiendo Ideas</div>
  </div>
  <p class="services">Tarjetas * Postales * Volantes *<br>* Folders * Revistas</p>
</section>

<section class="card card--white">
  <div class="brand">
    <div class="brand__row"><span class="brand__dot"></span><span class="brand__name">Timbrafix de México</span></div>
    <div class="brand__tagline">Imprimiendo Ideas</div>
  </div>
  <p class="services">Tarjetas * Postales * Volantes *<br>* Folders * Revistas</p>
</section>

<section class="card card--red">
  <div class="brand">
    <div class="brand__row"><span class="brand__dot"></span><span class="brand__name">Timbrafix de México</span></div>
    <div class="brand__tagline">Imprimiendo Ideas</div>
  </div>
  <p class="services">Tarjetas * Postales * Volantes *<br>* Folders * Revistas</p>
</section>

</body>
</html>
```